Start up business website

IT Support provider that caters towards law enforcement / police departments. We'll offer remote IT support, backup / recovery services and cyber security. Will add updates soon.

Target Market(s)

Police departments / Law Enforcement

Coding

Coded - Design and coding required

Number of Pages Required

5+ page

Font styles to use
Other font styles liked:
• Use font style in uploaded logo

Colors
0054AA
0677BA
7BADD7
CADEEF
E8F1F8

```html
<!DOCTYPE html>
<html lang="en">
<head>
<meta charset="utf-8">
<title>Bastion IT Support</title>
<link href="https://fonts.googleapis.com/css2?family=Orbitron:wght@500;700;900&family=Open+Sans:wght@400;600;700&display=swap" rel="stylesheet">
<style>
:root{
  --blue:#0054AA;
  --blue-mid:#0677BA;
  --blue-light:#7BADD7;
  --blue-pale:#CADEEF;
  --blue-mist:#E8F1F8;
  --navy:#0B1B36;
  --navy-deep:#07122A;
  --ink:#1B2433;
  --grey:#6B7583;
  --white:#FFFFFF;
}
*{margin:0;padding:0;box-sizing:border-box}
html,body{width:1200px;height:3680px;overflow:hidden}
body{font-family:"Open Sans",Arial,sans-serif;color:var(--ink);background:var(--white);position:relative}
.display{font-family:"Orbitron","Arial Black",sans-serif;text-transform:uppercase;font-weight:900;letter-spacing:1px}
section,header,footer{position:absolute;left:0;width:1200px}
.btn{display:inline-block;background:var(--blue);color:var(--white);font-size:12px;font-weight:700;letter-spacing:1px;text-transform:uppercase;padding:10px 20px;border-radius:2px}
.eyebrow{font-size:15px;text-transform:uppercase;letter-spacing:1px}

/* header */
.site-header{top:0;height:80px;background:var(--white);z-index:3}
.brand{position:absolute;left:24px;top:6px;height:68px;display:flex;align-items:center;gap:12px;padding:0 22px;background:var(--navy);border-radius:0 0 6px 6px}
.brand-mark{width:22px;height:22px;background:var(--blue)}
.brand-name{font-family:"Orbitron",sans-serif;font-weight:900;font-size:28px;color:var(--white);letter-spacing:2px}
.topbar{position:absolute;left:560px;right:0;top:0;height:30px;background:var(--navy);clip-path:polygon(20px 0,100% 0,100% 100%,0 100%);display:flex;align-items:center;gap:28px;padding-left:40px;font-size:12px;color:var(--blue-pale)}
.topbar .socials{display:flex;gap:10px;margin-left:auto;margin-right:40px}
.topbar .socials span{width:10px;height:10px;border-radius:50%;background:var(--blue-light)}
.main-nav{position:absolute;left:560px;top:42px;display:flex;gap:6px}
.main-nav a{font-size:12px;font-weight:600;color:var(--ink);text-transform:uppercase;padding:8px 16px;text-decoration:none}
.main-nav a.active{background:var(--blue);color:var(--white)}

/* hero */
.hero{top:30px;height:510px;background:linear-gradient(110deg,#0A1C3C 0%,#12305E 55%,#0A1B38 100%);overflow:hidden}
.hero-copy{position:absolute;left:128px;top:180px;color:var(--white);width:380px}
.hero-copy .eyebrow{font-size:18px;color:var(--blue-pale)}
.hero-copy h1{font-size:46px;line-height:1.05;margin-top:6px}
.hero-copy .sub{font-family:"Orbitron",sans-serif;font-weight:700;font-size:17px;letter-spacing:1px;text-transform:uppercase}
.hero-copy p{font-size:13px;line-height:1.55;color:var(--blue-pale);margin:14px 0 22px;width:300px}
.hero-art{position:absolute;left:600px;top:50px}

/* about */
.about{top:540px;height:570px;background:var(--white)}
.about-bar{position:absolute;left:132px;top:75px;width:12px;height:280px;background:var(--blue)}
.about-photo{position:absolute;left:190px;top:75px;width:400px;height:420px;background:radial-gradient(circle at 62% 55%,#2E7FC4 0%,#1A3E6E 35%,#0C1A30 80%)}
.about-copy{position:absolute;left:610px;top:120px;width:460px}
.about-copy .eyebrow{color:var(--ink);font-weight:600}
.about-copy h2{font-size:30px;line-height:1.25;margin:4px 0 20px}
.about-copy h2 .accent{color:var(--blue)}
.about-copy p{font-size:14px;line-height:1.65;color:var(--grey);margin-bottom:26px}

/* services */
.services{top:1110px;height:510px;background:linear-gradient(100deg,var(--blue) 0%,#0049A0 100%)}
.services-intro{position:absolute;left:128px;top:110px;width:440px;color:var(--white)}
.services-intro h2{font-size:34px;line-height:1.15;margin:6px 0 16px}
.services-intro p{font-size:13px;line-height:1.55;color:var(--blue-pale)}
.card{position:absolute;width:212px;height:160px;background:rgba(7,18,42,.35);border:1px solid rgba(123,173,215,.35);padding:22px 18px;color:var(--white)}
.card.featured{background:var(--white);color:var(--blue)}
.card .num{font-family:"Orbitron",sans-serif;font-weight:700;font-size:18px}
.card .icon{position:absolute;right:18px;top:22px}
.card h3{position:absolute;left:18px;bottom:20px;font-size:12px;font-weight:700;text-transform:uppercase;line-height:1.35;letter-spacing:.5px}

/* experience */
.experience{top:1620px;height:650px;background:var(--white)}
.experience h2{position:absolute;top:62px;width:100%;text-align:center;font-size:34px;font-style:italic;color:var(--blue)}
.experience h2 .dark{color:var(--navy)}
.live-photo{position:absolute;left:128px;top:140px;width:944px;height:440px;background:linear-gradient(100deg,#1B2636 0%,#2B3A4E 40%,#16283F 100%)}
.live-circle{position:absolute;left:850px;top:140px;width:440px;height:440px;margin-left:-210px;border-radius:50%;background:var(--blue);clip-path:inset(0 222px 0 0)}
.live-caption{position:absolute;left:720px;top:350px;color:var(--white)}
.live-caption .lead{font-size:20px;font-family:"Orbitron",sans-serif;font-weight:500;text-transform:uppercase}
.live-caption .big{font-size:36px;font-family:"Orbitron",sans-serif;font-weight:900;text-transform:uppercase;line-height:1.1}
.live-caption .more{font-size:12px;color:var(--blue-light);text-transform:uppercase;margin-top:8px;letter-spacing:1px}
.play{position:absolute;left:684px;top:240px;width:40px;height:40px;border-radius:50%;background:var(--white);display:flex;align-items:center;justify-content:center}

/* why choose */
.why{top:2270px;height:530px;background:linear-gradient(100deg,#0A1B3A 0%,#10284F 60%,#0A1A36 100%)}
.why-art{position:absolute;left:140px;top:70px}
.why-copy{position:absolute;left:530px;top:78px;width:470px;color:var(--white)}
.why-copy .eyebrow{color:var(--blue-pale)}
.why-copy h2{font-size:34px;line-height:1.15;margin:4px 0 18px}
.why-copy p{font-size:13px;line-height:1.6;color:var(--blue-pale);margin-bottom:18px}
.why-list{list-style:none;margin-bottom:26px}
.why-list li{font-size:13px;display:flex;align-items:center;gap:12px;margin-bottom:12px}
.why-list li::before{content:"";width:14px;height:14px;border-radius:50%;background:var(--blue-light)}

/* contact */
.contact{top:2800px;height:460px;background:var(--white)}
.contact-head{position:absolute;left:128px;top:72px}
.contact-head h2{font-size:34px;color:var(--blue);font-style:italic}
.contact-head p{font-size:13px;color:var(--grey);margin-top:6px}
.contact-form{position:absolute;left:128px;top:160px;width:480px;display:grid;grid-template-columns:1fr 1fr;gap:12px}
.field{height:40px;border:1px solid #C9D0DA;font-size:12px;color:var(--grey);padding:11px 12px}
.field.message{grid-column:1/3;height:110px}
.contact-form .btn{grid-column:2;justify-self:end}
.contact-photo{position:absolute;left:632px;top:80px;width:440px;height:320px;background:linear-gradient(110deg,#2A3B52 0%,#6A86A6 45%,#1D2C40 100%)}

/* footer */
.site-footer{top:3260px;height:420px;background:var(--navy-deep);color:var(--blue-pale)}
.footer-contacts{position:absolute;top:44px;left:128px;width:944px;display:flex;justify-content:space-between;font-size:12px}
.footer-contacts .item{display:flex;flex-direction:column;align-items:center;gap:10px;width:280px}
.footer-contacts .item svg{display:block}
.footer-rule{position:absolute;top:140px;left:128px;width:944px;height:1px;background:rgba(123,173,215,.3)}
.footer-brand{position:absolute;left:128px;top:210px;display:flex;align-items:center;gap:12px}
.footer-brand .brand-mark{width:24px;height:24px}
.footer-brand span{font-family:"Orbitron",sans-serif;font-weight:900;font-size:28px;color:var(--white);letter-spacing:2px}
.fcol{position:absolute;top:170px;font-size:12px;line-height:1.9}
.fcol h4{font-size:14px;color:var(--white);margin-bottom:8px;font-weight:700}
.news-input{width:190px;height:30px;background:var(--white);margin-bottom:8px;font-size:11px;color:var(--grey);padding:7px 10px}
.news-btn{width:190px;height:28px;background:var(--blue);color:var(--white);font-size:11px;font-weight:700;text-align:center;line-height:28px;text-transform:uppercase}
.follow{display:flex;gap:10px}
.follow span{width:22px;height:22px;border-radius:50%;background:var(--blue-pale)}
.copyright{position:absolute;bottom:18px;width:100%;text-align:center;font-size:11px;color:var(--blue-light)}
</style>
</head>
<body>

<header class="site-header">
  <div class="brand"><span class="brand-mark"></span><span class="brand-name">BASTION</span></div>
  <div class="topbar">
    <span>+1 (555) 010 4820</span>
    <span>info@bastionitsupport.com</span>
    <div class="socials"><span></span><span></span><span></span><span></span></div>
  </div>
  <nav class="main-nav">
    <a class="active">Home</a><a>About Us</a><a>Services</a><a>Support</a><a>News</a><a>Contact Us</a>
  </nav>
</header>

<section class="hero">
  <div class="hero-copy">
    <div class="eyebrow">Professional</div>
    <h1 class="display">Protection</h1>
    <div class="sub">With Reliable Service</div>
    <p>There are many variations of support plans, but the majority have suffered from slow response times.</p>
    <span class="btn">Get Started</span>
  </div>
  <svg class="hero-art" width="520" height="470" viewBox="0 0 520 470" role="img" aria-label="Photo of two IT specialists reviewing a tablet in a server room, framed in a shield shape">
    <defs>
      <linearGradient id="heroPhoto" x1="0" y1="0" x2="1" y2="1">
        <stop offset="0" stop-color="#3C6FA8"/><stop offset=".5" stop-color="#1F4576"/><stop offset="1" stop-color="#0E2446"/>
      </linearGradient>
    </defs>
    <path d="M60 20 Q260 0 470 30 L480 260 Q470 390 260 460 Q60 390 40 260 Z" fill="none" stroke="#0677BA" stroke-width="14"/>
    <path d="M72 34 Q260 16 458 42 L466 258 Q456 378 260 444 Q72 378 56 258 Z" fill="url(#heroPhoto)"/>
  </svg>
</section>

<section class="about">
  <div class="about-bar"></div>
  <div class="about-photo" role="img" aria-label="Close-up photo of an eye with a digital scanning overlay"></div>
  <div class="about-copy">
    <div class="eyebrow">We're the</div>
    <h2 class="display"><span class="accent">Best Agency</span> in<br>Downtown</h2>
    <p>We help departments keep their systems running around the clock. Our team handles remote support, secure backups and fast recovery so officers can stay focused on the work that matters most in the field and at the station.</p>
    <span class="btn">Read More</span>
  </div>
</section>

<section class="services">
  <div class="services-intro">
    <div class="eyebrow">Services</div>
    <h2 class="display">The Perfect<br>Solutions</h2>
    <p>We are committed to providing our customers with exceptional service while offering our employees the best training.</p>
  </div>
  <div class="card featured" style="left:608px;top:82px">
    <div class="num">01</div>
    <svg class="icon" width="34" height="34" viewBox="0 0 34 34"><path d="M17 3 L29 8 V17 Q29 27 17 31 Q5 27 5 17 V8 Z" fill="none" stroke="#0054AA" stroke-width="2"/></svg>
    <h3>Security<br>IT Services</h3>
  </div>
  <div class="card" style="left:848px;top:82px">
    <svg class="icon" width="34" height="34" viewBox="0 0 34 34"><path d="M17 3 L29 8 V17 Q29 27 17 31 Q5 27 5 17 V8 Z" fill="none" stroke="#CADEEF" stroke-width="2"/><rect x="12" y="15" width="10" height="8" fill="#CADEEF"/></svg>
    <h3>Data<br>Privacy</h3>
  </div>
  <div class="card" style="left:128px;top:270px">
    <svg class="icon" width="34" height="34" viewBox="0 0 34 34"><circle cx="17" cy="14" r="8" fill="none" stroke="#CADEEF" stroke-width="2"/><path d="M12 21 L10 31 L17 27 L24 31 L22 21" fill="none" stroke="#CADEEF" stroke-width="2"/></svg>
    <h3>Industry<br>Certified</h3>
  </div>
  <div class="card" style="left:368px;top:270px">
    <svg class="icon" width="34" height="34" viewBox="0 0 34 34"><rect x="4" y="6" width="26" height="18" fill="none" stroke="#CADEEF" stroke-width="2"/><path d="M12 30 H22 M17 24 V30" stroke="#CADEEF" stroke-width="2"/></svg>
    <h3>Network<br>Security Service</h3>
  </div>
  <div class="card" style="left:608px;top:270px">
    <svg class="icon" width="34" height="34" viewBox="0 0 34 34"><path d="M17 3 L29 8 V17 Q29 27 17 31 Q5 27 5 17 V8 Z" fill="none" stroke="#CADEEF" stroke-width="2"/><path d="M12 17 L16 21 L23 13" fill="none" stroke="#CADEEF" stroke-width="2"/></svg>
    <h3>Legal<br>Security Services</h3>
  </div>
  <div class="card" style="left:848px;top:270px">
    <svg class="icon" width="34" height="34" viewBox="0 0 34 34"><circle cx="17" cy="17" r="12" fill="none" stroke="#CADEEF" stroke-width="2"/><path d="M17 10 V17 L22 20" fill="none" stroke="#CADEEF" stroke-width="2"/></svg>
    <h3>Guarantee<br>Security Support</h3>
  </div>
</section>

<section class="experience">
  <h2 class="display">Experience <span class="dark">Us Live</span></h2>
  <div class="live-photo" role="img" aria-label="Photo of analysts working at monitors in a dark operations room"></div>
  <div class="live-circle"></div>
  <div class="play"><svg width="14" height="14" viewBox="0 0 14 14"><path d="M3 1 L12 7 L3 13 Z" fill="#0054AA"/></svg></div>
  <div class="live-caption">
    <div class="lead">Pursue Pleasure</div>
    <div class="big">Rationally</div>
    <div class="more">Discover More</div>
  </div>
</section>

<section class="why">
  <svg class="why-art" width="370" height="420" viewBox="0 0 370 420" role="img" aria-label="Photo of a technician at a laptop in front of server racks, framed in a shield shape">
    <defs>
      <linearGradient id="whyPhoto" x1="0" y1="0" x2="1" y2="1">
        <stop offset="0" stop-color="#4A7DB3"/><stop offset=".55" stop-color="#26507F"/><stop offset="1" stop-color="#122B4D"/>
      </linearGradient>
    </defs>
    <path d="M30 30 Q185 0 340 30 L350 230 Q340 340 185 410 Q30 340 20 230 Z" fill="#E8F1F8"/>
    <path d="M44 44 Q185 16 326 44 L335 228 Q326 328 185 394 Q44 328 35 228 Z" fill="url(#whyPhoto)"/>
  </svg>
  <div class="why-copy">
    <div class="eyebrow">Why Choose Us</div>
    <h2 class="display">Provide<br>Advanced Security</h2>
    <p>Our certified engineers monitor your network day and night, patch threats before they spread and restore lost data fast, so your department never loses critical records or time.</p>
    <ul class="why-list">
      <li>Contact Advisory Network</li>
      <li>Malware Detection Removal</li>
      <li>24/7 Support And Remote Admin</li>
    </ul>
    <span class="btn">Read More</span>
  </div>
</section>

<section class="contact">
  <div class="contact-head">
    <h2 class="display">Contact Us</h2>
    <p>Reach out and our support team will get back to you shortly.</p>
  </div>
  <div class="contact-form">
    <div class="field">First Name</div>
    <div class="field">Last Name</div>
    <div class="field">Email</div>
    <div class="field">Phone</div>
    <div class="field message">Message</div>
    <span class="btn">Submit</span>
  </div>
  <div class="contact-photo" role="img" aria-label="Photo of an engineer working at several monitors in an office"></div>
</section>

<footer class="site-footer">
  <div class="footer-contacts">
    <div class="item">
      <svg width="30" height="30" viewBox="0 0 30 30"><circle cx="15" cy="15" r="14" fill="#0054AA"/><path d="M15 7 Q20 7 20 12 Q20 16 15 23 Q10 16 10 12 Q10 7 15 7 Z" fill="#fff"/><circle cx="15" cy="12" r="2" fill="#0054AA"/></svg>
      <span>48 Harbor Lane, Westfield 20451</span>
    </div>
    <div class="item">
      <svg width="30" height="30" viewBox="0 0 30 30"><circle cx="15" cy="15" r="14" fill="#0054AA"/><path d="M10 8 L13 8 L14 12 L12 13 Q13 16 17 18 L18 16 L22 17 L22 20 Q21 22 18 21 Q11 18 9 11 Q9 8 10 8 Z" fill="#fff"/></svg>
      <span>+1 (555) 010 4820 | +1 (555) 010 4821</span>
    </div>
    <div class="item">
      <svg width="30" height="30" viewBox="0 0 30 30"><circle cx="15" cy="15" r="14" fill="#0054AA"/><rect x="8" y="10" width="14" height="10" fill="#fff"/><path d="M8 10 L15 16 L22 10" fill="none" stroke="#0054AA" stroke-width="1.5"/></svg>
      <span>info@bastionitsupport.com</span>
    </div>
  </div>
  <div class="footer-rule"></div>
  <div class="footer-brand"><span class="brand-mark"></span><span>BASTION</span></div>
  <div class="fcol" style="left:388px">
    <h4>Quick Links</h4>
    Home<br>About Us<br>Services<br>Support<br>Contact Us
  </div>
  <div class="fcol" style="left:540px">
    <h4>Services</h4>
    Security Services<br>Data Privacy<br>Network Security<br>Legal Services<br>Security Support
  </div>
  <div class="fcol" style="left:720px">
    <h4>Newsletter</h4>
    <div class="news-input">Your Email</div>
    <div class="news-btn">Subscribe</div>
  </div>
  <div class="fcol" style="left:932px">
    <h4>Follow Us</h4>
    <div class="follow"><span></span><span></span><span></span><span></span></div>
  </div>
  <div class="copyright">Copyright © 2024 Bastion IT Support. All Rights Reserved.</div>
</footer>

</body>
</html>
```